Meadowlark Dental Letterhead

Please design full color letterhead for meadowlark dental. Letterhead should match the motif of the business card. Print and logo should be confined to a one inch margin on top and bottom. The following info should be included:
Meadowlrk Dental with the tooth logo
Curtis R. Holloway, DDS
Gentle Hands, Bright Smiles Daily
Phone #: 918.555.0147
Address: 24813-C N Sycamore, Bixby, OK

```html
<!DOCTYPE html>
<html lang="en">
<head>
<meta charset="utf-8">
<title>Meadowlark Dental Letterhead</title>
<link href="https://fonts.googleapis.com/css2?family=Crimson+Text&family=Mulish:wght@400;700;800&display=swap" rel="stylesheet">
<style>
  :root {
    --page-bg: #ffffff;
    --canvas-bg: #ffffff;
    --frame: #3a3a3a;
    --brand-blue: #1a5fb4;
    --brand-red: #ff2a00;
    --brand-green: #12d600;
    --ink: #1a1a1a;
    --ink-soft: #333333;
  }
  html, body {
    margin: 0;
    padding: 0;
    width: 1200px;
    height: 1000px;
    overflow: hidden;
    background: var(--canvas-bg);
  }
  .letterhead {
    position: absolute;
    left: 229px;
    top: 16px;
    width: 740px;
    height: 958px;
    border: 1px solid var(--frame);
    background: var(--page-bg);
    overflow: hidden;
  }
  .header {
    position: absolute;
    left: 0;
    top: 0;
    width: 100%;
    height: 110px;
    border-bottom: 3px solid var(--brand-blue);
    box-shadow: 0 4px 5px rgba(0, 0, 0, 0.28);
  }
  .brand {
    position: absolute;
    left: 50px;
    top: 30px;
    width: 100px;
    text-align: center;
    font-family: "Mulish", sans-serif;
    font-weight: 700;
    color: var(--brand-blue);
    font-size: 13px;
    line-height: 14px;
    letter-spacing: 0.5px;
  }
  .brand-mark {
    display: block;
    width: 26px;
    height: 26px;
    margin: 0 auto 8px;
    background: var(--brand-blue);
  }
  .tagline {
    position: absolute;
    left: 287px;
    top: 89px;
    font-family: "Mulish", sans-serif;
    font-size: 7.5px;
    color: var(--ink);
    text-transform: uppercase;
  }
  .contact {
    position: absolute;
    right: 24px;
    top: 44px;
    text-align: right;
    font-family: "Mulish", sans-serif;
    font-style: normal;
    color: var(--ink-soft);
    font-size: 10px;
    line-height: 13px;
  }
  .contact .doctor {
    display: block;
    font-size: 17px;
    font-weight: 800;
    color: var(--brand-blue);
    line-height: 22px;
    margin-bottom: 1px;
  }
  .letter {
    position: absolute;
    left: 69px;
    top: 150px;
    width: 603px;
    font-family: "Crimson Text", serif;
    font-size: 14.1px;
    line-height: 17.1px;
    color: var(--ink);
    hyphens: auto;
    -webkit-hyphens: auto;
  }
  .letter p { margin: 0; }
  .letter .salutation { margin-bottom: 17.1px; }
  .footer-bands {
    position: absolute;
    left: 0;
    bottom: 0;
    width: 740px;
    height: 80px;
  }
  .footer-line {
    position: absolute;
    right: 24px;
    bottom: 9px;
    font-family: "Mulish", sans-serif;
    font-weight: 800;
    font-size: 24px;
    color: #ffffff;
  }
</style>
</head>
<body>
  <div class="letterhead">
    <header class="header">
      <div class="brand"><span class="brand-mark"></span>MEADOWLARK DENTAL</div>
      <div class="tagline">Gentle Hands, Bright Smiles Daily</div>
      <address class="contact">
        <span class="doctor">Curtis R. Holloway, D.D.S.</span>
        918-555-0147<br>
        24813-C N Sycamore,<br>
        Cedar Hollow, OK 74219
      </address>
    </header>

    <main class="letter">
      <p class="salutation">To whom it concerns:</p>
      <p>Volestr uptatus, corit lacestrum earis moditiis atus sed que nonseque natur? Quiberchil et qui nistrum dolor simin none que sandernatus consequ iduciis adit et exerrunt.</p>
      <p>Et vit officipis excest quis estiorro esequia spelestrum idem aspero molorrum rempe verovid iasinverio denesti onsecatio dolo quas dese mi, conem re parum aut est, que volorro tem facesseque pe voluptatem sedio ipicia deruptur anderfe ratur?</p>
      <p>Haria quias dit ape velit, conecuptas inctem conest, officia dusciam quatasimusa quis essequam dis volorrum fugit laut as di ommoditinus eum quae sit, quae quunt lam ilistru ptatemporum lab il eiur acimusam, quam alis ea sedit ist, nonsequis et qui con pre derum is dolor re nament quosape llantem oluptatus et debit fugiam, te qui qui voluptatque non nobitia tectae peri doluptu ribusa con pra quist modio to explate voluptatia qui utatet autem aut ex exerspiet volescitiae est accusaesedi dolest, quia nulparum veliquis voluptissit et ini rem adition secabo. Nequiate dolo volorecatur aut ommodipsam ut volum conseque excere lab imaiore laut reptasi modit, officto eatendi quost, unti consequ idempora volorehent, vollaut utemod qui omnistrum rem vent rerit et occabor re pa nonsedis ipitati orumqui aepudis coreiunto volliquatem natibus doluptae qui cusant.</p>
      <p>Soluptatias qui velest delliciis eaturiberunt laturio necuptis invelicipit, odigendam, sin cuptatur, tet hillaborum acerovitia quist, videbit a nihiliquam eles comnis quibusciae dicabore, te nis quam aut ligenim vollige ndicidenimus ex etur maxim quisci aut que volupta tquates etumet omnihic tes et at laut explabor simperum quo millam quibers pellabo. Diti dellam, que voluptas vernati berspiti cum erum quas audae. Dent que nes magnitist quae officta ne il experiaest, coritatem aditia sunti doluptae. Neque porepudit hillora tiistorro vid exerspe rferiatur min et ad quis ut facescimus, tem adissequam doluptiis sunt.</p>
      <p>Dolupta quae si utatur, sendunt alit molore volorro que rem harcia sum a doluptatem. Et exerum nobitatus pori asimolenda volorectet voluptio evernatem volore sed minvell essit, iurepresti blati voloribus eicium, comnienimin nonseque modit aut aut uta apel imillac caborrum, temporia verum que con eturent volenda ndistrunt del inctur aliciur? Rit quo veriame nderatur mo conseniet, officatqui doluptur? Os doluptat erepele cepero ipiet fugiatq uaspelit as audam lic to optas etur?</p>
      <p>Ulparum, occat quid ut es et que sed exeritet aut vitaqui accus nestiosandis magnihil ipsapel enimporro opta exeria ni iunt odit quias ex eictur? Ore, ad eum liquis re, volent exerro consecusam sincime niaeped ut fugit vendus ventur modia saepedit milluptatur am sit eles reiusti buscien ihitatiis arundae. Sedit ant.</p>
      <p>Ed que ea sunt, quide rem quistis que voluptatur sit volupta cus illenda vento blaborp oreptat emporen damendi in prore suntur?</p>
      <p>Berro te non plic temposam inum quiant.</p>
      <p>Ucium et es exeruptibus volupta int aligent fugiatur as eum harum rectur as autet laboren ihilit ducipsament prore volupta volum re, imperor eremporibus que laut et et pa vent.</p>
      <p>Illeseq uaepudae conectius eos con pratusciet audit estempe rferum fuga. Repedic tendis ipitatis ipsae. Iciumqui doles il es eatur?</p>
    </main>

    <svg class="footer-bands" viewBox="0 0 740 80" aria-hidden="true">
      <rect x="0" y="14" width="740" height="4" fill="var(--brand-red)"/>
      <rect x="0" y="24" width="740" height="8" fill="var(--brand-blue)"/>
      <rect x="0" y="38" width="740" height="42" fill="var(--brand-green)"/>
    </svg>
    <div class="footer-line">Caring For Every Smile</div>
  </div>
</body>
</html>
```